Ashford Church of Grace (this will be used for new church sign) sign will be 4'x8' and would like also listed Sunday School 9:00am Worship Service 10:30am.

Logo Text

ASHFORD CHURCH OF GRACE

```html
<!DOCTYPE html>
<html lang="en">
<head>
<meta charset="UTF-8">
<title>Ashford Church of Grace — Sign</title>
<link href="https://fonts.googleapis.com/css2?family=Bodoni+Moda:opsz,wght@6..96,400&family=Great+Vibes&family=Montserrat:wght@500&display=swap" rel="stylesheet">
<style>
  :root {
    --sky-deep: #03a0e2;
    --sky-mid: #5fc2ef;
    --sky-pale: #c9e9f8;
    --cloud: #ffffff;
    --title: #ffffff;
    --navy: #1b3f7c;
  }
  html, body {
    margin: 0;
    padding: 0;
    overflow: hidden;
    background: #ffffff;
  }
  .sign {
    position: relative;
    width: 1200px;
    height: 600px;
    overflow: hidden;
    background: linear-gradient(155deg, var(--sky-deep) 0%, var(--sky-mid) 40%, var(--sky-pale) 72%, var(--cloud) 100%);
  }
  .church-name {
    position: absolute;
    left: 66px;
    top: 42px;
    margin: 0;
    font-family: "Bodoni Moda", serif;
    font-weight: 400;
    font-size: 98px;
    line-height: 93px;
    letter-spacing: 1px;
    color: var(--title);
  }
  .church-name .line { display: block; white-space: nowrap; }
  .church-name .connector {
    font-family: "Great Vibes", cursive;
    font-size: 78px;
    letter-spacing: 0;
    position: relative;
    top: 22px;
    margin-left: 4px;
  }
  .hill-scene {
    position: absolute;
    left: 0;
    top: 0;
    width: 1200px;
    height: 600px;
  }
  .dove-art {
    position: absolute;
    left: 778px;
    top: 182px;
    width: 126px;
    height: 144px;
    border-radius: 50% 40% 45% 50%;
    background: radial-gradient(circle at 45% 50%, rgba(255,255,255,0.85), rgba(255,255,255,0.25));
  }
  .crucifix-art {
    position: absolute;
    left: 906px;
    top: 64px;
    width: 252px;
    height: 340px;
    border-radius: 8px;
    background: linear-gradient(180deg, rgba(255,255,255,0.75), rgba(255,255,255,0.95));
  }
  .schedule {
    position: absolute;
    left: 88px;
    top: 448px;
    height: 62px;
    display: flex;
    align-items: center;
    gap: 8px;
    font-family: "Montserrat", sans-serif;
    font-weight: 500;
    font-size: 20.5px;
    letter-spacing: 0.6px;
    color: var(--navy);
    white-space: nowrap;
  }
  .schedule .divider { width: 34px; height: 62px; display: block; }
</style>
</head>
<body>
  <main class="sign">
    <svg class="hill-scene" role="img" aria-label="Soft white hilltop rising toward the right" viewBox="0 0 1200 600" xmlns="http://www.w3.org/2000/svg">
      <defs>
        <linearGradient id="hillFade" x1="0" y1="1" x2="1" y2="0">
          <stop offset="0" stop-color="#ffffff" stop-opacity="0.6"/>
          <stop offset="0.35" stop-color="#ffffff" stop-opacity="1"/>
        </linearGradient>
      </defs>
      <path d="M405 600 C 520 585, 600 545, 700 520 C 790 495, 840 430, 880 415 C 930 395, 960 395, 1010 390 C 1060 386, 1110 400, 1150 420 C 1175 430, 1190 440, 1200 445 L 1200 600 Z" fill="url(#hillFade)"/>
    </svg>

    <div class="dove-art" role="img" aria-label="Illustration of a dove carrying an olive branch"></div>
    <div class="crucifix-art" role="img" aria-label="Illustration of a crucifix standing on the hilltop"></div>

    <h1 class="church-name">
      <span class="line">ASHFORD</span>
      <span class="line">CHURCH<span class="connector">of</span></span>
      <span class="line">GRACE</span>
    </h1>

    <p class="schedule">
      <span class="service">SUNDAY SCHOOL 09:00AM</span>
      <svg class="divider" viewBox="0 0 34 62" aria-hidden="true" xmlns="http://www.w3.org/2000/svg">
        <rect x="14" y="0" width="6" height="62" fill="#ffffff"/>
        <rect x="0" y="15" width="34" height="5" fill="#ffffff"/>
      </svg>
      <span class="service">WORSHIP SERVICE 10:30AM</span>
    </p>
  </main>
</body>
</html>
```